Business Card

I want our business cards to have a little more pizzazz. I like the content, and we are in healthcare (so nothing to wild or artsy), but something that allows our cards to stand out.

Business

```html
<!DOCTYPE html>
<html lang="en">
<head>
<meta charset="utf-8">
<title>Veralis Medical Supply – Business Card</title>
<link href="https://fonts.googleapis.com/css2?family=Lato:wght@400;700&display=swap" rel="stylesheet">
<style>
  :root {
    --brand-blue: #1d5a8f;
    --band-grey: #8a8f94;
    --paper: #ffffff;
    --backdrop: #e6e6e6;
    --ink-light: #ffffff;
  }
  * { margin: 0; padding: 0; box-sizing: border-box; }
  html, body {
    width: 1200px; height: 1086px; overflow: hidden;
    background: var(--backdrop);
    font-family: "Lato", Arial, sans-serif;
  }
  .canvas { position: relative; width: 1200px; height: 1086px; }

  .card {
    position: absolute; left: 254px; width: 677px; height: 387px;
    border-radius: 6px; overflow: hidden;
  }
  .card-front { top: 126px; background: var(--paper); color: var(--brand-blue); }
  .card-back { top: 586px; background: var(--brand-blue); color: var(--ink-light); }

  .wordmark {
    position: absolute; display: flex; align-items: center; gap: 12px;
    font-weight: 700; line-height: 1.02;
  }
  .wordmark-dot { width: 40px; height: 40px; border-radius: 50%; flex: none; }
  .wordmark-name { font-size: 34px; }
  .wordmark-sub { display: block; font-size: 21px; letter-spacing: 2.4px; }
  .card-front .wordmark { left: 50px; top: 163px; color: var(--brand-blue); }
  .card-front .wordmark-dot { background: var(--brand-blue); }
  .card-back .wordmark { left: 54px; top: 161px; color: var(--ink-light); }
  .card-back .wordmark-dot { background: var(--ink-light); }

  .divider { position: absolute; width: 2px; }
  .card-front .divider { left: 336px; top: 82px; height: 228px; background: var(--brand-blue); }
  .card-back .divider { left: 342px; top: 150px; height: 88px; background: var(--ink-light); }

  .contact { position: absolute; left: 360px; top: 76px; }
  .contact-name { font-size: 27px; font-weight: 700; line-height: 1.1; }
  .contact-title { font-size: 17px; margin-top: 1px; }
  .contact-list { list-style: none; margin-top: 29px; }
  .contact-list li {
    display: flex; align-items: center; gap: 6px;
    font-size: 19px; line-height: 23px;
  }
  .contact-list svg { width: 20px; height: 18px; fill: var(--brand-blue); flex: none; }
  .contact-address { font-size: 19px; line-height: 23px; margin-top: 16px; }

  .front-band-line { position: absolute; left: 0; right: 0; top: 360px; height: 4px; background: var(--band-grey); }
  .front-band { position: absolute; left: 0; right: 0; top: 364px; bottom: 0; background: var(--brand-blue); }

  .services { position: absolute; left: 354px; top: 147px; list-style: none; }
  .services li {
    display: flex; align-items: center; gap: 8px;
    font-size: 19px; line-height: 23px;
  }
  .services svg { width: 22px; height: 20px; flex: none; }

  .hotline {
    position: absolute; left: 0; right: 0; top: 290px;
    text-align: center; font-size: 19px; line-height: 23px;
  }
</style>
</head>
<body>
<div class="canvas">

  <section class="card card-front">
    <div class="wordmark">
      <span class="wordmark-dot"></span>
      <span class="wordmark-name">Veralis Medical<span class="wordmark-sub">SUPPLY</span></span>
    </div>
    <div class="divider"></div>
    <div class="contact">
      <h1 class="contact-name">Daniel Reyes</h1>
      <p class="contact-title">Territory Manager</p>
      <ul class="contact-list">
        <li><svg viewBox="0 0 20 18"><path d="M2 7c0-3 4-5 8-5s8 2 8 5v2h-4V7H6v2H2z"/><rect x="4" y="9" width="12" height="7" rx="1"/></svg>(555) 210-4416</li>
        <li><svg viewBox="0 0 20 18"><rect x="5" y="1" width="10" height="5"/><rect x="1" y="6" width="18" height="7" rx="1"/><rect x="5" y="11" width="10" height="6"/></svg>(555) 249-0172</li>
        <li><svg viewBox="0 0 20 20"><circle cx="10" cy="10" r="8.5" fill="none" stroke="#1d5a8f" stroke-width="1.6"/><ellipse cx="10" cy="10" rx="3.8" ry="8.5" fill="none" stroke="#1d5a8f" stroke-width="1.4"/><path d="M1.5 10h17M3 6h14M3 14h14" stroke="#1d5a8f" stroke-width="1.3"/></svg>www.veralismed.com</li>
        <li><svg viewBox="0 0 20 16"><rect x="1" y="2" width="18" height="12" fill="#1d5a8f"/><path d="M1 2l9 7 9-7M1 14l7-6M19 14l-7-6" fill="none" stroke="#fff" stroke-width="1.2"/></svg>daniel.reyes@veralismed.com</li>
      </ul>
      <p class="contact-address">48 Harbor Lane Fairview<br>NJ 07000 . 555.447.3100</p>
    </div>
    <div class="front-band-line"></div>
    <div class="front-band"></div>
  </section>

  <section class="card card-back">
    <div class="wordmark">
      <span class="wordmark-dot"></span>
      <span class="wordmark-name">Veralis Medical<span class="wordmark-sub">SUPPLY</span></span>
    </div>
    <div class="divider"></div>
    <ul class="services">
      <li><svg viewBox="0 0 22 20"><rect x="1" y="4" width="15" height="15" fill="#fff"/><path d="M4 11l4 4 12-13" fill="none" stroke="#1d5a8f" stroke-width="4"/><path d="M4 11l4 4 12-13" fill="none" stroke="#fff" stroke-width="2"/></svg>Servicing Laboratories</li>
      <li><svg viewBox="0 0 22 20"><rect x="1" y="4" width="15" height="15" fill="#fff"/><path d="M4 11l4 4 12-13" fill="none" stroke="#1d5a8f" stroke-width="4"/><path d="M4 11l4 4 12-13" fill="none" stroke="#fff" stroke-width="2"/></svg>Hospital &amp; Medical centers</li>
      <li><svg viewBox="0 0 22 20"><rect x="1" y="4" width="15" height="15" fill="#fff"/><path d="M4 11l4 4 12-13" fill="none" stroke="#1d5a8f" stroke-width="4"/><path d="M4 11l4 4 12-13" fill="none" stroke="#fff" stroke-width="2"/></svg>Reserch Facilities</li>
      <li><svg viewBox="0 0 22 20"><rect x="1" y="4" width="15" height="15" fill="#fff"/><path d="M4 11l4 4 12-13" fill="none" stroke="#1d5a8f" stroke-width="4"/><path d="M4 11l4 4 12-13" fill="none" stroke="#fff" stroke-width="2"/></svg>surgical Centers</li>
    </ul>
    <p class="hotline">If you can’t reach me, please call our<br>Customer Service Hotline at 555.447.3111</p>
  </section>

</div>
</body>
</html>
```